Stylish Business Card for Modern hair salon

I need a simple business card design using our salon logo and colours that are in the logo. We service clients of all ages but predominantly those in the 18 to 55 age range. We have a young staff and are looking to have a card that will present a modern and clean image that represents who we are. The card should be in black and white same as our logo. Minimal use of other colours is allowed.

Industry/Entity Type

Hair And Beauty

Contact Information for Business Card

The design should have the following information
salon name - TZ Hair Studio
address - 2957 Fernbrook Rd.W. Mississauga, ON L8R3P2
phone - 905 641-2087
website - tzhairexample.ca
instagram - tz.hairstudio
twitter - @TZ_HairStudio

Colors
000000
ffffff
474747

Requirements
Must have
• simple design, salon name, address, phone, website, instagram, twitter info
• Back of card should have the following:
• YOUR NEXT APPOINTMENT
• DATE
• TIME
Nice to have
• simple design, clear to see and read,
• predominantly black and white colour, minimal use of other colours is ok
Should not have
• many colours, various fonts

```html
<!DOCTYPE html>
<html lang="en">
<head>
<meta charset="utf-8">
<title>TZ Hair Studio – Appointment Card</title>
<link rel="stylesheet" href="https://fonts.googleapis.com/css2?family=Bodoni+Moda:opsz,wght@6..96,400&display=swap">
<style>
  :root {
    --ink: #000000;
    --paper: #ffffff;
    --grey: #474747;
  }
  * { margin: 0; padding: 0; box-sizing: border-box; }
  html, body {
    width: 1200px;
    height: 686px;
    overflow: hidden;
    background: var(--paper);
  }
  .card {
    position: relative;
    width: 1200px;
    height: 686px;
    background: var(--paper);
    color: var(--ink);
    font-family: "Bodoni Moda", "Didot", serif;
    font-weight: 400;
  }
  .card-frame {
    position: absolute;
    left: 23px;
    top: 23px;
    width: 1154px;
    height: 640px;
    border: 2px solid var(--ink);
  }
  .appointment-label {
    position: absolute;
    right: 583px;
    font-size: 42px;
    line-height: 1;
    white-space: nowrap;
  }
  .appointment-label.date { top: 94px; }
  .appointment-label.time { top: 144px; }
  .write-line {
    position: absolute;
    left: 648px;
    width: 413px;
    height: 0;
    border-top: 1.5px solid var(--ink);
  }
  .write-line.date { top: 129px; }
  .write-line.time { top: 179px; }
  .salon-name {
    position: absolute;
    left: 0;
    width: 1200px;
    top: 290px;
    text-align: center;
    font-size: 66px;
    line-height: 1;
    color: var(--ink);
    white-space: nowrap;
  }
  .contact-list {
    position: absolute;
    left: 0;
    width: 1200px;
    top: 458px;
    list-style: none;
    text-align: center;
    font-size: 34px;
    line-height: 38px;
  }
</style>
</head>
<body>
  <main class="card">
    <div class="card-frame"></div>

    <p class="appointment-label date">Your Next Appointment:</p>
    <div class="write-line date"></div>
    <p class="appointment-label time">Time:</p>
    <div class="write-line time"></div>

    <h1 class="salon-name">TZ Hair Studio</h1>

    <ul class="contact-list">
      <li>2957 Fernbrook Rd.W. Mississauga, ON L8R3P2</li>
      <li>Phone - 905 641-2087</li>
      <li>Website - tzhairexample.ca</li>
      <li>Instagram - tz.hairstudio</li>
      <li>Twitter - @TZ_HairStudio</li>
    </ul>
  </main>
</body>
</html>
```